Rack Card for IV Infusion Vitamin Supplement bar

We need a very eye catching rack card so that customers would instantly know it is for IV vitamin infusions. We have our previous rack card (pdf) as an example that did not bring in any clients as an example as well as another one that we did not like too much. The bar is for people to feel better with hydration and vitamins.

Target Market(s)

Anyone

Industry/Entity Type

Healthcare

Requirements
Must have
• Logo on rack card
Should not have
• Not pink other than the logo

```html
<!DOCTYPE html>
<html lang="en">
<head>
<meta charset="utf-8">
<title>Willow Health &amp; Wellness – IV Infusion Rack Card</title>
<link href="https://fonts.googleapis.com/css2?family=Marcellus&family=Lora:ital,wght@0,400;0,700;1,700&display=swap" rel="stylesheet">
<style>
  :root{
    --green:#0c4f42;
    --green-light:#6f9c8f;
    --cream:#f1efe4;
    --paper:#ffffff;
    --ink:#1d1d1d;
    --muted:#555;
    --bg:#cfcfcf;
  }
  *{box-sizing:border-box;margin:0;padding:0}
  html,body{width:676px;height:1200px;overflow:hidden}
  body{background:linear-gradient(#e6e6e6,#c4c4c4);font-family:"Lora",serif;position:relative}

  .card{position:absolute;top:274px;width:300px;height:652px;overflow:hidden;box-shadow:0 6px 18px rgba(0,0,0,.25)}
  .card--front{left:25px;background:var(--paper)}
  .card--back{left:351px;background:radial-gradient(ellipse at 60% 45%,#fbfaf4 0%,var(--cream) 70%,#e6e3d3 100%)}

  /* front */
  .front-shape{position:absolute;inset:0}
  .photo{position:absolute;left:10px;top:0;width:220px;height:220px;border-radius:50%;border:4px solid #fff;
    background:radial-gradient(circle at 60% 40%,#f7f7f7,#d8dadc 60%,#b9bec0);}
  .title{position:absolute;left:0;right:0;top:226px;text-align:center;color:#fff;font-family:"Marcellus",serif;font-size:27px;line-height:33px}
  .fruit{position:absolute;left:18px;top:312px;width:266px;height:126px;border-radius:50%;
    background:radial-gradient(ellipse at 45% 55%,#f7a531 0%,#f08b1c 40%,rgba(170,200,220,.8) 70%,rgba(255,255,255,0) 78%)}
  .tagline{position:absolute;left:0;right:0;top:444px;text-align:center;font-size:14.5px;line-height:21px;color:var(--ink)}
  .tagline em{font-weight:700;font-style:italic}
  .tagline .soft{color:var(--muted)}
  .brand{position:absolute;left:0;right:0;top:526px;display:flex;align-items:center;justify-content:center;gap:6px;
    font-family:"Marcellus",serif;color:var(--green);font-size:20px;letter-spacing:3px}
  .brand-dot{width:10px;height:10px;border-radius:50%;background:var(--green)}
  .front-contact{position:absolute;left:0;right:0;bottom:0;height:69px;border-radius:70px 70px 0 0;
    background:linear-gradient(90deg,var(--green) 55%,#2c6b5d);color:#fff;text-align:center;padding-top:9px}
  .phone{font-family:"Lora",serif;font-weight:700;font-size:26px;line-height:30px}
  .web{font-size:10.5px;letter-spacing:1.6px;margin-top:2px}

  /* back */
  .bar{position:absolute;left:16px;width:268px;height:35px;border-radius:3px;color:#fff;font-family:"Marcellus",serif;
    background:linear-gradient(90deg,#2e6c5e,var(--green) 45%,var(--green) 65%,#4d8577);
    display:flex;align-items:center;justify-content:center;font-size:17px}
  .bar--small{font-family:"Lora",serif;font-size:11.5px}
  .offers{position:absolute;left:19px;top:63px;width:262px;display:grid;grid-template-columns:1fr 1fr;column-gap:12px;font-size:7.6px;line-height:11.2px;color:#333}
  .offer{margin-bottom:11px}
  .offer h3{font-size:7.6px;font-weight:700;text-transform:uppercase;color:#222}
  .offer--short{margin-bottom:8px}
  .addons{position:absolute;left:19px;top:438px;width:262px;display:grid;grid-template-columns:1.1fr 1fr;font-size:7.6px;line-height:13px;font-weight:700;color:#222}
  .back-phone{position:absolute;left:0;right:0;top:571px;text-align:center;color:var(--green);font-weight:700;font-size:26px}
  .address{position:absolute;left:0;right:0;top:610px;text-align:center;font-size:11px;letter-spacing:1.6px;line-height:15px;color:#222}
</style>
</head>
<body>
  <section class="card card--front">
    <svg class="front-shape" viewBox="0 0 300 652" aria-hidden="true">
      <defs>
        <linearGradient id="greenFade" x1="0" x2="1">
          <stop offset="0.55" stop-color="#0c4f42"/>
          <stop offset="1" stop-color="#2f6e60"/>
        </linearGradient>
      </defs>
      <path d="M0 16 H250 A50 50 0 0 1 300 66 V300 A150 82 0 0 1 0 300 Z" fill="url(#greenFade)"/>
    </svg>
    <div class="photo" role="img" aria-label="Photo of a nurse starting an IV drip on a smiling client in a white robe"></div>
    <h1 class="title">IV Infusion Vitamin<br>Supplement Bar</h1>
    <div class="fruit" role="img" aria-label="Fresh oranges with a splash of water"></div>
    <p class="tagline"><em>Recharge, Revitalize, &amp; Rejuvenate</em><br>Your Body for <span class="soft">a Healthier,</span><br>Happier <span class="soft">You!</span></p>
    <div class="brand"><span class="brand-dot"></span>WILLOW</div>
    <div class="front-contact">
      <div class="phone">555 - 210 -4477</div>
      <div class="web">www.willowtotalhealth.com</div>
    </div>
  </section>

  <section class="card card--back">
    <h2 class="bar" style="top:13px">What we offer?</h2>
    <div class="offers">
      <div>
        <div class="offer"><h3>Willow Cocktail</h3>Reduce stress, fatigue, and boost your energy. Willow client favorite! (IV fluids, Vitamin C, B-complex, B12, and electrolytes)</div>
        <div class="offer"><h3>Immune Support</h3>Protect the immune system when risk of illness is high. Great for pre, post-travel (IV fluids, Vitamin C, B-complex, and Zinc)</div>
        <div class="offer"><h3>The Glow</h3>Give a glowing boost to skin and hair from inside out. (IV fluids, Glutathione, Vitamin B-complex, and Biotin)</div>
        <div class="offer"><h3>NAD+ 125G/ 250G/ 500G Drip</h3>Enhance your cognitive health and help reverse aging. Promotes cell regeneration. Can aid mental clarity, better sleep, and energy.</div>
      </div>
      <div>
        <div class="offer"><h3>Sports Recovery</h3>Recover fast from illness, exhaustion, and workouts. (IV fluids, B-complex, B12, and amino acids, and electrolytes)</div>
        <div class="offer"><h3>Energized</h3>Boost metabolism, burn fat easier, and feel energized. (IV fluids, B-complex, and amino acid blend)</div>
        <div class="offer"><h3>Brain Power</h3>Support overall brain function, increase memory recall and improve certain aspects of learning. (IV fluids, B6, alpha lipoic acid, and taurine)</div>
        <div class="offer offer--short"><h3>The Jetlag Drip</h3></div>
        <div class="offer offer--short"><h3>The Migraine / PMS Drip</h3></div>
        <div class="offer offer--short"><h3>The Hangover Drip</h3></div>
        <div class="offer"><h3>High Dose Vitamin C</h3>*Medical clearance required</div>
      </div>
    </div>
    <h2 class="bar" style="top:384px">Infusion add-ons</h2>
    <div class="addons">
      <ul style="list-style:none">
        <li>Glutathione</li><li>Additional Vitamin C</li><li>Additional Zinc</li><li>Additional Magnesium</li><li>Anti- Inflammation Medication</li>
      </ul>
      <ul style="list-style:none">
        <li>Anti-nausea Medication</li><li>Vitamin D Shot</li><li>Vitamin B12 Shot</li>
      </ul>
    </div>
    <p class="bar bar--small" style="top:523px">By appointments only, including weekends</p>
    <div class="back-phone">555 - 210 -4477</div>
    <address class="address" style="font-style:normal">1200 N. Elm St Suite 2B<br>Riverton, IN 46000</address>
  </section>
</body>
</html>
```